Webdesign für Onlineshop
Zielgruppe
Wir verkaufen in unserem Onlineshop alles zum Thema Wohnen mit dem Schwerpunkt Möbel. Die Hauptzielgruppe ist zwischen 25 und 45 Jahren.
Aufgabenstellung
Wir bevorzugen ein modernes, flaches und aufgeräumtes Design ähnlich wie velm.de / dorano88.de mit dem Fokus auf Preisaggressivität und Rabatte.
- Das Grundlayout muss so bleiben, wie es aktuell ist. Natürlich dürfen einzelne Elemente verschoben / versetzt werden.
- Im Header sollte Platz für eine kleine Werbefläche sein (ähnlich wie der konfigurierbare Kleiderschrank).
- Der Shop basiert auf Magento 1.9.
- Die Rabatte in den Produktdetailseiten müssen genauso aufgebaut sein
- Die Suche sollte in den Header platziert werden und nicht im Menü
- Ein SSL Logo soll im Header platziert weden
- Die Vorteile (Kostenloser Versand, Sicher einkaufen, Kauf auf Rechnung) sollen im Header erscheinen
- Das Design sollte responsive sein
Es wird nur das reine Design ohne Programmierung benötigt.

```html
<!DOCTYPE html>
<html lang="de">
<head>
<meta charset="utf-8">
<title>quellmark3berg – Möbel Online Shop</title>
<link href="https://fonts.googleapis.com/css2?family=Open+Sans:wght@300;400;600;700&display=swap" rel="stylesheet">
<style>
:root{
  --green:#7ba83c;
  --teal:#3aa7bf;
  --magenta:#c3185c;
  --text:#333;
  --muted:#777;
  --line:#e3e3e3;
  --light:#f2f2f2;
  --white:#fff;
}
*{box-sizing:border-box;margin:0;padding:0}
html,body{width:1200px;height:4161px;overflow:hidden}
body{position:relative;background:var(--white);font-family:"Open Sans",sans-serif;color:var(--text)}
.section{position:absolute;left:0;width:1200px}
.wrap{position:relative;width:862px;margin:0 auto;height:100%}

/* top bar */
.topbar{top:0;height:83px;background:var(--light)}
.topbar .phone{position:absolute;left:0;top:22px;display:flex;align-items:center;gap:10px}
.topbar .phone-num{color:var(--teal);font-size:19px;font-weight:600;line-height:20px}
.topbar .phone-hours{font-size:11px;color:var(--muted)}
.promo{position:absolute;left:255px;top:4px;width:353px;height:72px;background:var(--white);display:flex;align-items:center;justify-content:center;gap:14px}
.promo .pct{font-size:40px;font-weight:600;color:var(--green)}
.promo .txt{font-size:13px;line-height:15px}
.promo .txt small{display:block;font-size:9px;color:var(--muted)}
.promo .txt b{display:block;color:var(--green);font-size:10px;letter-spacing:.5px}
.badges{position:absolute;right:0;top:12px;display:flex;gap:14px;align-items:center}
.badge-plain{width:36px;height:36px;border-radius:50%;background:#c9c9c9}
.badge-sq{width:30px;height:36px;background:#c9c9c9}
.badge-bar{position:absolute;right:10px;top:50px;width:140px;height:10px;background:var(--green)}

/* header */
.header{top:83px;height:137px;border-bottom:1px solid var(--line)}
.logo{position:absolute;left:0;top:48px;display:flex;align-items:center;gap:8px;font-size:28px;font-weight:700;color:var(--green)}
.logo i{width:14px;height:14px;background:var(--green);display:block}
.search{position:absolute;left:252px;top:53px;width:356px;height:38px;border:1px solid var(--line);display:flex;align-items:center;gap:10px;padding-left:14px;font-size:13px;color:var(--muted)}
.h-icons{position:absolute;right:40px;top:54px;display:flex;gap:46px}
.cart-count{position:absolute;right:-12px;top:-10px;width:22px;height:22px;border-radius:50%;background:var(--teal);color:#fff;font-size:13px;font-weight:600;text-align:center;line-height:22px}

/* nav */
.nav{top:220px;height:60px;border-bottom:1px solid var(--line)}
.nav ul{list-style:none;display:flex;justify-content:space-between;height:60px;align-items:stretch}
.nav li{font-size:12px;display:flex;align-items:center;padding:0 10px}
.nav li.active{background:var(--teal);color:#fff;padding:0 30px}

/* hero */
.hero{top:280px;height:452px;background:linear-gradient(100deg,#b7b4ae 0%,#9f9a93 40%,#c4c0ba 70%,#d7d4cf 100%)}
.hero h1{position:absolute;left:216px;top:58px;color:#fff;font-size:44px;line-height:52px;font-weight:700}
.btn{display:inline-block;background:var(--green);color:#fff;font-weight:600;font-size:19px;text-align:center}
.hero .btn{position:absolute;left:218px;top:189px;width:193px;height:50px;line-height:50px}
.arrow-c{position:absolute;width:30px;height:30px;border-radius:50%;background:#fff;display:flex;align-items:center;justify-content:center}
.dots{position:absolute;left:560px;top:416px;display:flex;gap:8px}
.dots span{width:15px;height:15px;border-radius:50%;border:2px solid #fff}
.dots span.on{background:var(--green);border-color:var(--green)}

/* benefits */
.benefits{top:765px;height:85px}
.benefits .wrap{display:flex}
.benefit{flex:1;display:flex;align-items:center;justify-content:center;gap:30px;font-size:15px}
.benefit+.benefit{border-left:1px solid var(--line)}

/* banners */
.banners{top:879px;height:296px}
.banners .wrap{display:flex;justify-content:space-between}
.banner{position:relative;width:424px;height:296px}
.banner h2{position:absolute;left:36px;top:140px;color:#fff;font-size:25px;line-height:30px;font-weight:700}
.banner .btn{position:absolute;left:36px;top:218px;width:148px;height:46px;line-height:46px;font-size:18px}

/* product rows */
.row-head{position:absolute;left:0;top:0;font-size:30px;font-weight:300;letter-spacing:.3px}
.row-nav{position:absolute;right:0;top:-6px;display:flex;gap:14px}
.row-nav span{width:46px;height:46px;border:1px solid var(--line);border-radius:50%;display:flex;align-items:center;justify-content:center}
.products{position:absolute;left:0;top:54px;width:862px;display:flex;justify-content:space-between}
.product{width:205px;position:relative}
.product .img{height:140px}
.disc{position:absolute;left:-6px;top:-6px;width:46px;height:46px;border-radius:50%;background:var(--magenta);color:#fff;font-size:14px;font-weight:600;text-align:center;line-height:46px}
.product .name{margin:16px 12px 0;font-size:12px;line-height:16px;color:var(--muted);height:48px}
.product .old{margin:6px 12px 0;font-size:11px;color:var(--muted);text-decoration:line-through}
.product .price{margin:0 12px;font-size:20px;color:var(--magenta)}
.price.teal{color:var(--teal)}

/* kids promo */
.kids{top:1614px;height:340px}
.kids .box{position:absolute;inset:0;border:1px solid var(--line);overflow:hidden}
.kids .img{position:absolute;right:0;top:0;width:470px;height:100%;background:linear-gradient(90deg,#fff 0%,#ece6e0 30%,#d7cbc0 60%,#b7c9d7 100%)}
.kids h2{position:absolute;left:55px;top:33px;font-size:32px;font-weight:400}
.kids p{position:absolute;left:55px;top:86px;width:340px;font-size:14px;line-height:22px;color:var(--muted)}
.kids .amount{position:absolute;left:55px;top:156px;font-size:50px;color:var(--teal);font-weight:400}
.kids .btn{position:absolute;left:55px;top:240px;width:167px;height:46px;line-height:46px;font-size:18px}

/* SEO text */
.seo{top:2832px;height:600px}
.seo h2{text-align:center;font-size:28px;font-weight:300}
.seo .cols{position:absolute;left:0;top:60px;width:862px;display:flex;justify-content:space-between}
.seo .col{width:410px}
.seo h3{font-size:16px;font-weight:600;margin:14px 0 6px}
.seo p{font-size:10.5px;line-height:15px;color:#555;margin-bottom:8px}

/* newsletter */
.newsletter{top:3474px;height:184px;background:var(--light)}
.newsletter .intro{position:absolute;left:112px;top:50px;font-size:16px;line-height:22px;font-weight:300;color:#555}
.newsletter .field{position:absolute;left:112px;top:133px;width:432px;height:40px;background:#fff;font-size:11px;line-height:40px;padding-left:20px}
.newsletter .submit{position:absolute;left:544px;top:133px;width:208px;height:40px;background:var(--teal);color:#fff;font-weight:700;font-size:15px;text-align:center;line-height:40px}
.tag{position:absolute;left:625px;top:28px;width:100px;height:54px;background:var(--green);color:#fff;font-weight:700;font-size:13px;line-height:15px;text-align:center;padding-top:11px;transform:rotate(40deg)}

/* feature boxes */
.features{top:3692px;height:94px}
.features .wrap{display:flex;justify-content:space-between}
.feature{position:relative;width:282px;height:94px;border:1px solid var(--line);padding:14px 16px}
.feature h4{color:var(--teal);font-size:16px;font-weight:400}
.feature p{font-size:9px;color:var(--muted);margin-top:8px;line-height:12px}
.feature .img{position:absolute;right:12px;top:16px;width:84px;height:62px}

/* payment band */
.payments{top:3804px;height:60px;background:var(--teal)}
.payments .wrap{display:flex;align-items:center;justify-content:space-around;padding:0 90px}
.payments span{color:#fff;font-weight:600;font-size:14px}
.payments i{display:block;width:60px;height:12px;background:rgba(255,255,255,.45)}

/* footer */
.footer{top:3885px;height:210px}
.fcol{position:absolute;top:0;font-size:12px}
.fcol h5{font-size:12px;font-weight:400;margin-bottom:10px}
.fcol li{list-style:none;font-size:9px;line-height:18px;color:#555}
.fcol .hl{color:var(--teal);font-size:10px}
.fcol .sm{font-size:9px;color:#555;line-height:13px;margin-bottom:10px}
.social{display:flex;gap:12px}
.social span{width:28px;height:28px;border-radius:50%;background:var(--teal)}
.seal{position:absolute;width:58px;height:58px;border-radius:50%;background:#d1d1d1}
.rating{position:absolute;left:765px;top:20px;color:var(--teal);font-size:15px;line-height:17px}
.rating small{display:block;color:var(--muted);font-size:10px}
.legal{position:absolute;left:765px;top:118px;width:150px;font-size:7px;line-height:9px;color:var(--muted)}
.foot-note{position:absolute;top:4118px;left:0;width:1200px;text-align:center;font-size:9px;color:#999}
</style>
</head>
<body>

<header class="section topbar">
  <div class="wrap">
    <div class="phone">
      <svg width="30" height="30" viewBox="0 0 30 30"><circle cx="15" cy="15" r="13" fill="none" stroke="#3aa7bf" stroke-width="2"/><path d="M10 9c1-1 2-1 3 1l1 2-2 2c1 2 3 4 5 5l2-2 2 1c2 1 2 2 1 3-2 2-5 2-9-2s-5-8-3-10z" fill="#3aa7bf"/></svg>
      <div><div class="phone-num">0571 / 47 21 63 90</div><div class="phone-hours">Mo-Fr 9-21 Uhr Sa 10-15 Uhr</div></div>
    </div>
    <div class="promo">
      <span class="pct">10%</span>
      <div class="txt">Kleiderschrank jetzt<small>auch selbst zusammenstellen</small><b>EINFÜHRUNGSRABATTE</b></div>
    </div>
    <div class="badges"><span class="badge-plain"></span><span class="badge-plain"></span><span class="badge-sq"></span></div>
    <span class="badge-bar"></span>
  </div>
</header>

<div class="section header">
  <div class="wrap">
    <div class="logo">quellmark3berg<i></i></div>
    <div class="search">
      <svg width="14" height="14" viewBox="0 0 14 14"><circle cx="6" cy="6" r="4.5" fill="none" stroke="#555" stroke-width="1.5"/><path d="M9.5 9.5L13 13" stroke="#555" stroke-width="1.5"/></svg>
      Suche...
    </div>
    <div class="h-icons">
      <svg width="28" height="30" viewBox="0 0 28 30"><circle cx="14" cy="9" r="6" fill="none" stroke="#333" stroke-width="1.8"/><path d="M3 28c0-7 5-11 11-11s11 4 11 11z" fill="none" stroke="#333" stroke-width="1.8"/></svg>
      <svg width="30" height="30" viewBox="0 0 30 30"><path d="M3 3h12l12 12-12 12L3 15z" fill="none" stroke="#333" stroke-width="1.8"/><circle cx="9" cy="9" r="2" fill="#333"/></svg>
      <div style="position:relative"><svg width="32" height="30" viewBox="0 0 32 30"><path d="M2 4h5l4 16h15l3-11H9" fill="none" stroke="#333" stroke-width="1.8"/><circle cx="13" cy="26" r="2" fill="#333"/><circle cx="24" cy="26" r="2" fill="#333"/></svg><span class="cart-count">3</span></div>
    </div>
  </div>
</div>

<nav class="section nav">
  <div class="wrap">
    <ul>
      <li>WOHNEN</li><li class="active">SCHLAFEN</li><li>KINDER-BABY</li><li>ESSEN</li><li>KUCHE</li><li>BIS 60% RABATT</li><li>SONSTIGES</li><li>SALE</li>
    </ul>
  </div>
</nav>

<section class="section hero">
  <div role="img" aria-label="Helles Schlafzimmer mit Bett, Kleiderschrank und Steinwand" style="position:absolute;inset:0"></div>
  <h1>Matratzen mit Komfort<br>für mehr Schlafqualität</h1>
  <span class="btn">40% GESPART</span>
  <span class="arrow-c" style="left:82px;top:212px"><svg width="10" height="10" viewBox="0 0 10 10"><path d="M7 1L3 5l4 4" fill="none" stroke="#333" stroke-width="1.5"/></svg></span>
  <span class="arrow-c" style="left:1086px;top:212px"><svg width="10" height="10" viewBox="0 0 10 10"><path d="M3 1l4 4-4 4" fill="none" stroke="#333" stroke-width="1.5"/></svg></span>
  <div class="dots"><span></span><span class="on"></span><span></span><span></span></div>
</section>

<section class="section benefits">
  <div class="wrap">
    <div class="benefit">
      <svg width="50" height="40" viewBox="0 0 50 40"><path d="M4 8h26v22H4zM30 16h9l7 7v7H30z" fill="none" stroke="#3aa7bf" stroke-width="2"/><circle cx="12" cy="32" r="4" fill="#fff" stroke="#3aa7bf" stroke-width="2"/><circle cx="38" cy="32" r="4" fill="#fff" stroke="#3aa7bf" stroke-width="2"/></svg>
      Kostenloser Versand
    </div>
    <div class="benefit">
      <svg width="34" height="42" viewBox="0 0 34 42"><path d="M9 16V10a8 8 0 0116 0v6" fill="none" stroke="#3aa7bf" stroke-width="2"/><rect x="3" y="16" width="28" height="24" rx="3" fill="none" stroke="#3aa7bf" stroke-width="2"/><path d="M11 28l5 5 8-9" fill="none" stroke="#3aa7bf" stroke-width="2"/></svg>
      Sicher einkaufen
    </div>
    <div class="benefit">
      <svg width="38" height="42" viewBox="0 0 38 42"><rect x="4" y="3" width="28" height="36" fill="none" stroke="#3aa7bf" stroke-width="2"/><path d="M10 12h16M10 19h16M10 26h12" stroke="#3aa7bf" stroke-width="2"/></svg>
      Kauf auf Rechnung
    </div>
  </div>
</section>

<section class="section banners">
  <div class="wrap">
    <div class="banner">
      <div role="img" aria-label="Offener Kleiderschrank mit bunter Kleidung" style="position:absolute;inset:0;background:linear-gradient(90deg,#6f5a4e,#b78a6a 40%,#c9a58c 60%,#5f6d86)"></div>
      <h2>Ihr ganz persönlicher<br>Kleiderschrank</h2>
      <span class="btn">40% GESPART</span>
    </div>
    <div class="banner">
      <div role="img" aria-label="Wohnzimmer mit schwarzem Ledersessel vor großem Fenster" style="position:absolute;inset:0;background:linear-gradient(90deg,#3b3b3b,#7c7f84 45%,#b9bcc0 70%,#4a4a4a)"></div>
      <h2>Ihr ganz persönlicher<br>Kleiderschrank</h2>
      <span class="btn">40% GESPART</span>
    </div>
  </div>
</section>

<section class="section" style="top:1225px;height:340px">
  <div class="wrap">
    <h2 class="row-head">UNSERE TOPSELLER</h2>
    <div class="row-nav"><span><svg width="12" height="12" viewBox="0 0 12 12"><path d="M11 6H2M5 3L2 6l3 3" fill="none" stroke="#888" stroke-width="1.3"/></svg></span><span><svg width="12" height="12" viewBox="0 0 12 12"><path d="M1 6h9M7 3l3 3-3 3" fill="none" stroke="#888" stroke-width="1.3"/></svg></span></div>
    <div class="products">
      <div class="product"><div class="img" role="img" aria-label="Schwarzes Boxspringbett" style="background:linear-gradient(#e8e8e8,#7a7a7a)"></div><span class="disc">-36%</span><p class="name">Wohnlandschaft, in Mikrofaser Vintage-Look braun</p><p class="old">999,00 €</p><p class="price">575,10 €</p></div>
      <div class="product"><div class="img" role="img" aria-label="Schlafzimmer in Eiche-Dekor mit türkiser Bettwäsche" style="background:linear-gradient(#8c7a68,#7fc2c7 70%,#c9b69a)"></div><span class="disc">-27%</span><p class="name">Schlafzimmerkombination 4-tlg. in Eiche-Dekor mit Abs. in Lavagrau</p><p class="old">999,00 €</p><p class="price">575,10 €</p></div>
      <div class="product"><div class="img" role="img" aria-label="Weißer Esstisch mit grauen Stühlen" style="background:linear-gradient(#b9c2c8,#7d8187)"></div><span class="disc">-12%</span><p class="name">Boxspringbett schwarz, Feinstrukturstoff</p><p class="old">999,00 €</p><p class="price">575,10 €</p></div>
      <div class="product"><div class="img" role="img" aria-label="Braunes Sofa vor weißer Wand" style="background:linear-gradient(#f0f0f0 50%,#6b4a37)"></div><span class="disc">-34%</span><p class="name">Boxspringbett schwarz, Feinstrukturstoff</p><p class="old">999,00 €</p><p class="price">575,10 €</p></div>
    </div>
  </div>
</section>

<section class="section kids">
  <div class="wrap">
    <div class="box">
      <div class="img" role="img" aria-label="Mutter und Tochter lächeln gemeinsam"></div>
      <h2>Kindgerecht und schön!</h2>
      <p>Entdecken Sie unsere kindgerechten Baby- und Kinderzimmer und zaubern Sie ihren Kleinen ein wundervolles Lächeln ins Gesicht!</p>
      <div class="amount">445,47 €</div>
      <span class="btn">40% GESPART</span>
    </div>
  </div>
</section>

<section class="section" style="top:2014px;height:340px">
  <div class="wrap">
    <h2 class="row-head">NEU IM SORTIMENT</h2>
    <div class="row-nav"><span><svg width="12" height="12" viewBox="0 0 12 12"><path d="M11 6H2M5 3L2 6l3 3" fill="none" stroke="#888" stroke-width="1.3"/></svg></span><span><svg width="12" height="12" viewBox="0 0 12 12"><path d="M1 6h9M7 3l3 3-3 3" fill="none" stroke="#888" stroke-width="1.3"/></svg></span></div>
    <div class="products">
      <div class="product"><div class="img" role="img" aria-label="Weißes Bett mit roter Decke" style="background:linear-gradient(#d6d6d6,#b3242e 70%,#eee)"></div><span class="disc">-36%</span><p class="name">Wohnlandschaft, in Mikrofaser Vintage-Look braun</p><p class="old">999,00 €</p><p class="price">575,10 €</p></div>
      <div class="product"><div class="img" role="img" aria-label="Helles Holzbett im Schlafzimmer" style="background:linear-gradient(#cbb9a4,#e9dfd2)"></div><p class="name">Boxspringbett schwarz, Feinstrukturstoff</p><p class="old">999,00 €</p><p class="price teal">575,10 €</p></div>
      <div class="product"><div class="img" role="img" aria-label="Kleiderschrank in Eiche" style="background:linear-gradient(#b3834f,#8c6236)"></div><p class="name">Boxspringbett schwarz, Feinstrukturstoff</p><p class="old">999,00 €</p><p class="price teal">575,10 €</p></div>
      <div class="product"><div class="img" role="img" aria-label="Schwarzes Boxspringbett" style="background:linear-gradient(#ececec,#555)"></div><p class="name">Boxspringbett schwarz, Feinstrukturstoff</p><p class="old">999,00 €</p><p class="price teal">575,10 €</p></div>
    </div>
  </div>
</section>

<section class="section" style="top:2416px;height:340px">
  <div class="wrap">
    <h2 class="row-head">BELIEBTE ARTIKEL</h2>
    <div class="row-nav"><span><svg width="12" height="12" viewBox="0 0 12 12"><path d="M11 6H2M5 3L2 6l3 3" fill="none" stroke="#888" stroke-width="1.3"/></svg></span><span><svg width="12" height="12" viewBox="0 0 12 12"><path d="M1 6h9M7 3l3 3-3 3" fill="none" stroke="#888" stroke-width="1.3"/></svg></span></div>
    <div class="products">
      <div class="product"><div class="img" role="img" aria-label="Nachttisch in Eiche" style="background:linear-gradient(#e8e2da,#b98a55)"></div><p class="name">Wohnlandschaft, in Mikrofaser Vintage-Look braun</p><p class="old">999,00 €</p><p class="price teal">575,10 €</p></div>
      <div class="product"><div class="img" role="img" aria-label="Graues Polsterbett" style="background:linear-gradient(#cfcfcf,#9a9a9a)"></div><p class="name">Boxspringbett schwarz, Feinstrukturstoff</p><p class="old">999,00 €</p><p class="price teal">575,10 €</p></div>
      <div class="product"><div class="img" role="img" aria-label="Kinderzimmer mit Schrank und Bett" style="background:linear-gradient(#8a6a4c,#6fbcc4 80%)"></div><span class="disc">-36%</span><p class="name">Boxspringbett schwarz, Feinstrukturstoff</p><p class="old">999,00 €</p><p class="price">575,10 €</p></div>
      <div class="product"><div class="img" role="img" aria-label="Bett mit roter Decke" style="background:linear-gradient(#3b3b3b,#eee 50%,#b0242c)"></div><p class="name">Boxspringbett schwarz, Feinstrukturstoff</p><p class="old">999,00 €</p><p class="price teal">575,10 €</p></div>
    </div>
  </div>
</section>

<section class="section seo">
  <div class="wrap">
    <h2>Möbel im Online Shop von quellmark3berg</h2>
    <div class="cols">
      <div class="col">
        <h3>Immer modern, hochwertig &amp; günstig</h3>
        <p>Der Name des Online Shops quellmark3berg ist Programm: Hier finden Sie stilvolle Möbel, Accessoires und weiteres Zubehör für das Leben in den eigenen vier Wänden. Überzeugen Sie sich selbst, entdecken Sie unser großes Sortiment an modernen Möbelstücken und richten Sie Ihre Wohnung stilvoll ein!</p>
        <h3>So finden Sie Ihre Traummöbel</h3>
        <p>Vergeuden Sie keine Zeit mehr mit der mühsamen Suche im lokalen Möbelhaus. Im Online Shop von quellmark3berg finden Sie zu jeder Zeit und auf schnelle Weise moderne Möbel zum günstigen Preis. Vom Wohnzimmer über die Küche bis hin zum Jugendzimmer, ob Bad oder Esszimmer – ganz gleich, für welchen Wohnraum Sie eine neue Einrichtung suchen, mit der übersichtlichen Navigation und dem praktischen Suchfilter finden Sie Möbelstücke, die Ihren Anforderungen entsprechen. Wählen Sie einfach Material, Farbe, Maße und Ihr gewünschtes Budget aus. In Sekundenschnelle erhalten Sie eine breite Auswahl an Möbeln.</p>
        <h3>Möbel direkt vom Hersteller</h3>
        <p>In unserem Shop können Sie moderne Wohnwände, Polstermöbel, Schränke und weitere Wohnzimmermöbel günstig online bestellen. Unser Produktportfolio enthält Möbel direkt vom Hersteller, wodurch wir den Kunden unsere Artikel zu Top Konditionen anbieten können. Außerdem profitieren Sie von einer hochwertigen Qualität, einem trendigen Design und dem ausgezeichneten Service von quellmark3berg.</p>
        <h3>Unser großes Möbel Angebot - Entdecken Sie die Vielfalt</h3>
        <p>Es gibt eine Vielzahl an Maßen, Farben und Materialien, die in der Summe ein unterschiedliches Design hervorrufen. Dabei hat jeder Mensch seinen ganz eigenen Geschmack. Damit wir auch Ihre Vorliebe in Sachen Wohnungseinrichtung treffen, finden Sie in unserem Online Shop ein großes Angebot an Möbeln in unterschiedlichen Stilrichtungen.</p>
      </div>
      <div class="col">
        <p style="margin-top:14px">Sie suchen nach einem bequemen Fernseh-Sessel in einem coolen Design? Dann empfehlen wir Ihnen unseren Relax Sessel im schwarzen Kunstleder und mit einer verstellbaren Rückenlehne. Ein kleiner Hocker ist ebenso in der Lieferung enthalten und sorgt für zusätzlichen Liegekomfort. Selbstverständlich bieten wir Ihnen passend zu diesem Möbelstück Sideboards, Stühle, Wandregale, Sofas und Co. an. Mit quellmark3berg können Sie Ihr Wohnzimmer in einem einheitlichen Stil einrichten.</p>
        <p>Auch für das Schlafzimmer finden Sie eine Vielzahl an unterschiedlichen Betten, Kleiderschränken, Nachttischen sowie weiteren Schlafzimmermöbeln. Überzeugen Sie sich selbst und bestellen Sie Ihre gewünschten Möbel günstig in unserem Online Shop!</p>
        <h3>Möbel für Babys und Kinder</h3>
        <p>In unserem Shop finden Sie eine große Auswahl an Kindermöbeln. Wir bieten Ihnen komplette Babyzimmer und Jugendzimmer Sets, mit denen Sie das Zimmer Ihres Kindes im handumdrehen wunschgerecht und günstig einrichten. Dabei legen wir hohe Maßstäbe an die Qualität der Möbel und stehen Ihnen mit unserem kompetenten Service gerne beratend zur Seite.</p>
        <h3>Unser Service</h3>
        <p>Bei Fragen stehen wir Ihnen gerne zur Verfügung. Schreiben Sie uns einfach eine E-Mail oder kontaktieren Sie unsere Service-Mitarbeiter telefonisch. Wir helfen Ihnen gerne bei der Auswahl Ihrer Wunschmöbel.</p>
        <p>Neben unserer kompetenten Beratung profitieren Sie auch von unserem zuverlässigen Lieferservice ohne Aufpreis.</p>
        <p>Außerdem bieten wir Ihnen mehrere zuverlässige Zahlarten an. Sie entscheiden, ob Sie per Banküberweisung, Paylino, Nachnahme, Kreditkarte, Rechnungskauf oder per Finanzierung zahlen wollen.</p>
      </div>
    </div>
  </div>
</section>

<section class="section newsletter">
  <div class="wrap">
    <p class="intro">Kostenlosen Newsletter abonnieren, von zahlreichen<br>Aktionen profitieren und einen kostenlosen Einkaufsgutschein</p>
    <div class="field">Ihre E-mail adresse</div>
    <div class="submit">JETZT SICHERN!</div>
    <div class="tag">5€<br>Gutschein</div>
  </div>
</section>

<section class="section features">
  <div class="wrap">
    <div class="feature"><h4>Versandkostenfrei</h4><p>Ohne Aufpreis.<br>Nutzen Sie unser Angebot!</p><div class="img" role="img" aria-label="Weißer Lieferwagen" style="background:linear-gradient(#f4f4f4,#c8c8c8)"></div></div>
    <div class="feature"><h4>0571 / 47 21 63 90</h4><p>Ohne Aufpreis.<br>Nutzen Sie unser Angebot!</p><div class="img" role="img" aria-label="Service-Mitarbeiterin mit Headset" style="background:linear-gradient(#f3ebe4,#d9b9a0)"></div></div>
    <div class="feature"><h4>Unschlagbaren Preisen</h4><p>Direkt vom Hersteller</p><div class="img" role="img" aria-label="Türkises Sparschwein mit Münze" style="background:linear-gradient(#eaf6f8,#8fd0dc)"></div></div>
  </div>
</section>

<section class="section payments">
  <div class="wrap">
    <span>Paylino</span><span>Kartoro</span><span>Direktano</span><span>Vantrax</span><span>Rechnung</span><i></i><i></i><i></i>
  </div>
</section>

<footer class="section footer">
  <div class="wrap">
    <div class="fcol" style="left:0"><h5>Kundenservice</h5><ul><li>Zahlungsarten</li><li>Lieferung</li><li>AGB</li><li>Widerrufsrecht</li><li>Datenschutz</li><li>Katalog</li><li>Blog</li></ul></div>
    <div class="fcol" style="left:119px"><h5>Über uns</h5><ul><li>Über uns</li><li>Kontakt</li><li>Impressum</li></ul></div>
    <div class="fcol" style="left:207px"><h5>Folge uns auf</h5><div class="social"><span></span><span></span></div></div>
    <div class="fcol" style="left:340px;width:130px"><h5>Einfach und sicher</h5><p class="hl">Bestellvorgang</p><p class="sm">Schnell, übersichtlich und mit SSL-Datenschutz</p><p class="hl">Lieferung</p><p class="sm">Kostenlose Lieferung innerhalb Deutschland.</p></div>
    <span class="seal" style="left:640px;top:12px"></span>
    <span class="seal" style="left:700px;top:12px"></span>
    <div class="rating">4.25/5<br>★★★★★<small>Sehr gut</small></div>
    <span class="seal" style="left:640px;top:100px"></span>
    <p class="legal">Eine kontinuierliche Überwachung durch spezialisierte Anwälte stellt sicher, dass unsere Kunden vollständig und korrekt über ihre Rechte aufgeklärt werden.</p>
  </div>
</footer>

<p class="foot-note">Preisangaben inkl. gesetzl. MwSt. und zzgl. Service- und Versandkosten</p>

</body>
</html>
```